Energy Drink Concept and Design--Vorta Brisk

This is a concept we are workshopping so have fun!! Get as creative or out there as you want. Short contest as we have a presentation deadline for Monday 4/18. This doesnt have to be perfect, just get your ideas out there for me!

Think ZapHorn or Kestrel. This is an energy drink in a can.

We do expect it to be a bit more natural with no artificial flavors or sweeteners. Probably lower calorie as well.

Drink it it and get a Ninja power boost for you day. What does a Ninja represent to you? What will get guys to drink this?

Feel free to add copy or design elements you see fit. We are leaving this quite open on purpose as we want many diverse concepts. Once we chose a direction we will revise accordingly. Dont worry about nutritional content or ingredients, just put placeholders.

Inspiration here:
https://www.vidplexo.example/watch?v=qT7mxb_kwP2

Target Market(s)

Aimed at the 18 to 34 male segment, including Gamers.

Requirements
Must have
• Great looking, creative design.

```html
<!DOCTYPE html>
<html lang="en">
<head>
<meta charset="utf-8">
<title>Vorta Brisk Energy Drink – Can Label</title>
<link rel="stylesheet" href="https://fonts.googleapis.com/css2?family=Arimo:wght@400;700&family=Ma+Shan+Zheng&display=swap">
<style>
  :root {
    --stage-light: #f4f4f4;
    --stage-mid: #c9c9c9;
    --label-black: #000;
    --sun-red: #c8100a;
    --shade-red: #8e0905;
    --ink-white: #fff;
    --ink-dark: #111;
  }
  * { box-sizing: border-box; margin: 0; padding: 0; }
  html, body { width: 1200px; height: 960px; overflow: hidden; }
  body {
    position: relative;
    background: linear-gradient(180deg, var(--stage-mid) 0%, var(--stage-light) 25%, var(--stage-light) 75%, var(--stage-mid) 100%);
    font-family: "Arimo", Arial, sans-serif;
  }
  .can-label {
    position: absolute; left: 38px; top: 222px; width: 1106px; height: 508px;
    background: var(--label-black); color: var(--ink-white); overflow: hidden;
  }
  .product-intro { position: absolute; left: 81px; top: 27px; width: 290px; }
  .product-intro h2 { font-size: 13px; font-weight: 700; margin-bottom: 3px; }
  .product-intro p { font-size: 10.5px; line-height: 12.6px; }

  .nutrition-panel {
    position: absolute; left: 79px; top: 95px; width: 275px; height: 227px;
    background: var(--ink-white); color: var(--ink-dark);
    border: 2px solid var(--ink-white); outline: 1px solid var(--ink-dark); outline-offset: -4px;
    padding: 4px 5px; font-size: 4.6px; line-height: 8px; overflow: hidden;
  }
  .nf-grid { display: grid; grid-template-columns: 108px 1fr 1fr 1fr; column-gap: 4px; }
  .nf-title { font-size: 12.5px; font-weight: 700; line-height: 14px; white-space: nowrap; }
  .nf-col-head { line-height: 5.5px; border-bottom: 1px solid var(--ink-dark); padding-bottom: 1px; }
  .nf-row { display: contents; }
  .nf-row > span { border-bottom: 0.6px solid #777; display: flex; justify-content: space-between; white-space: nowrap; overflow: hidden; }
  .nf-thick > span { border-bottom: 3px solid var(--ink-dark); }
  .nf-b { font-weight: 700; }
  .nf-in { padding-left: 7px; }

  .ingredients { position: absolute; left: 192px; top: 337px; width: 168px; font-size: 10.5px; line-height: 12.8px; }
  .distributor { position: absolute; left: 192px; top: 426px; font-size: 10.5px; line-height: 12.8px; }
  .origin { position: absolute; left: 192px; top: 470px; font-size: 10.5px; }

  .front-art { position: absolute; left: 0; top: 0; width: 1106px; height: 508px; }
  .brand-line {
    position: absolute; font-family: "Ma Shan Zheng", serif; color: var(--ink-white);
    font-size: 100px; line-height: 1; white-space: nowrap;
  }
  .brand-line--top { left: 634px; top: 122px; }
  .brand-line--bottom { left: 698px; top: 214px; }
  .tagline { position: absolute; left: 740px; top: 312px; font-family: "Ma Shan Zheng", serif; font-size: 24px; white-space: nowrap; }
  .volume { position: absolute; left: 712px; top: 450px; width: 156px; text-align: center; font-family: "Ma Shan Zheng", serif; font-size: 19px; white-space: nowrap; }
</style>
</head>
<body>
<section class="can-label">
  <div class="product-intro">
    <h2>Vorta Brisk Drink:</h2>
    <p>Lorem ipsum dolor sit amet, consectetuer adipiscing elit, sed diam nonummy nibh euismod tincidunt ut laoreet dolore magna aliquam erat volutpat.</p>
  </div>

  <div class="nutrition-panel">
    <div class="nf-grid">
      <div class="nf-title">Nutrition Facts</div>
      <div class="nf-col-head">Wheat Squares Sweetened</div>
      <div class="nf-col-head">Corn Flakes Not Sweetened</div>
      <div class="nf-col-head">Mixed Grain Flakes Sweetened</div>
      <div class="nf-row nf-thick"><span>Serving Size 1 box / Per Container</span><span>(35g)</span><span>(19g)</span><span>(27g)</span></div>
      <div class="nf-row"><span class="nf-b">Amount Per Serving</span><span></span><span></span><span></span></div>
      <div class="nf-row"><span class="nf-b">Calories</span><span>130</span><span>70</span><span>100</span></div>
      <div class="nf-row nf-thick"><span class="nf-in">Calories from Fat</span><span>0</span><span>0</span><span>0</span></div>
      <div class="nf-row"><span class="nf-b">Total Fat</span><span>0g <b>0%</b></span><span>0g <b>0%</b></span><span>0g <b>0%</b></span></div>
      <div class="nf-row"><span class="nf-in">Saturated Fat</span><span>0g <b>0%</b></span><span>0g <b>0%</b></span><span>0g <b>0%</b></span></div>
      <div class="nf-row"><span class="nf-in">Trans Fat</span><span>0g</span><span>0g</span><span>0g</span></div>
      <div class="nf-row"><span class="nf-b">Cholesterol</span><span>0mg <b>0%</b></span><span>0mg <b>0%</b></span><span>0mg <b>0%</b></span></div>
      <div class="nf-row"><span class="nf-b">Sodium</span><span>0mg <b>0%</b></span><span>200mg <b>8%</b></span><span>120mg <b>5%</b></span></div>
      <div class="nf-row"><span class="nf-b">Potassium</span><span>125mg <b>4%</b></span><span>25mg <b>1%</b></span><span>30mg <b>1%</b></span></div>
      <div class="nf-row"><span class="nf-b">Total Carbohydrate</span><span>29g <b>10%</b></span><span>17g <b>6%</b></span><span>24g <b>8%</b></span></div>
      <div class="nf-row"><span class="nf-in">Dietary Fiber</span><span>3g <b>12%</b></span><span>1g <b>4%</b></span><span>1g <b>4%</b></span></div>
      <div class="nf-row"><span class="nf-in">Sugars</span><span>8g</span><span>6g</span><span>13g</span></div>
      <div class="nf-row nf-thick"><span class="nf-b">Protein</span><span>4g</span><span>1g</span><span>1g</span></div>
      <div class="nf-row"><span>*Percent Daily Values are based</span><span>Vitamin A 0%</span><span>10%</span><span>10%</span></div>
      <div class="nf-row"><span>on a 2,000 calorie diet.</span><span>Vitamin C 0%</span><span>15%</span><span>90%</span></div>
      <div class="nf-row"><span>Your values may be higher or lower.</span><span>Calcium 0%</span><span>0%</span><span>0%</span></div>
      <div class="nf-row"><span>Total Fat less than 65g 80g</span><span>Iron 10%</span><span>6%</span><span>20%</span></div>
      <div class="nf-row"><span>Sodium less than 2,400mg</span><span>Thiamin 10%</span><span>15%</span><span>20%</span></div>
      <div class="nf-row"><span>Potassium 3,500mg</span><span>Riboflavin 30%</span><span>15%</span><span>20%</span></div>
      <div class="nf-row"><span>Total Carbohydrate 300g 375g</span><span>Niacin 30%</span><span>15%</span><span>20%</span></div>
      <div class="nf-row"><span>Dietary Fiber 25g 30g</span><span>Vitamin B6 30%</span><span>15%</span><span>20%</span></div>
    </div>
  </div>

  <p class="ingredients">Carbonated Water, Sucrose, Glucose, Sodium Citrate Taurine,Glucuronolactone, Caffrinr, Instol, Miacinamode, Calcium Pantothenate, Pyridoxine, HCL, Vitamin b12</p>
  <p class="distributor">Distributed By:<br>Vorta Brisk .N.A, INC.<br>Harbor Vale, CA 90512</p>
  <p class="origin">Made in Austria</p>

  <svg class="front-art" viewBox="0 0 1106 508">
    <defs>
      <clipPath id="sun-clip"><circle cx="852" cy="224" r="182"/></clipPath>
    </defs>
    <circle cx="852" cy="224" r="182" fill="var(--sun-red)"/>
    <g clip-path="url(#sun-clip)">
      <rect role="img" aria-label="Bamboo stalks and leaves along the right side of the sun" x="900" y="40" width="140" height="380" fill="var(--shade-red)" opacity="0.6"/>
      <ellipse role="img" aria-label="Silhouette of a ninja crouching on the top of the sun" cx="848" cy="92" rx="44" ry="40" fill="var(--shade-red)" opacity="0.75"/>
    </g>
  </svg>
  <div class="brand-line brand-line--top">Vorta</div>
  <div class="brand-line brand-line--bottom">Brisk</div>
  <div class="tagline">Energy Drink</div>
  <div class="volume">8.3 FL. OZ [250ml.]</div>
</section>
</body>
</html>
```